FRESH WEB DESIGN FOR A HEALTH - SOCIAL NETWORK

We are currently looking for a creative, fresh, vibrant, inspiring design for a new social network focused on health and nutrition for health professionals (namely nutritionists) and end-users.

Design requirements - IMPORTANT: please see attached file 'LumaGrove web site design scope' for the detailed brief.

The web site requires new design templates with inter-changeable banners and in some cases profile images. It's important for the website to communicate LumaGrove's core values and image which includes fun, vitality, freshness, life fulfillment, trust, integrity and loyalty to the two target groups. Imagery must have a consistent/inter-related theme across all communities, topics and resources, which need to be easily applied to the web site.To help engage our audience we are looking for something fresh and unique in the selected imagery/ theme/ design templates.

The chosen design will need to be applied to create a PDF, PowerPoint and business card template.

Please see attached file 'LumaGrove web site design scope' to view the LumaGrove web site, which is currently under development.

Industry/Entity Type

Nutrition

```html
<!DOCTYPE html>
<html lang="en">
<head>
<meta charset="utf-8">
<title>LumaGrove — Health &amp; Nutrition Network</title>
<link rel="stylesheet" href="https://fonts.googleapis.com/css2?family=Jost:wght@400;500&family=Open+Sans:wght@400;600;700&display=swap">
<style>
  :root{
    --green:#a9cf3b;
    --green-dark:#8dbf2e;
    --green-soft:#c9d77c;
    --blue:#2aa3dc;
    --blue-deep:#1d8fcc;
    --ink:#1e1e1e;
    --grey:#8a8a8a;
    --grey-light:#d9d9d9;
    --white:#ffffff;
    --footer:#afd13f;
  }
  *{box-sizing:border-box;margin:0;padding:0}
  html,body{width:1200px;height:2778px;overflow:hidden}
  body{position:relative;background:var(--white);font-family:"Open Sans",Arial,sans-serif;color:var(--ink)}
  .abs{position:absolute}

  /* header */
  .site-header{left:0;top:0;width:1200px;height:130px;background:linear-gradient(180deg,#f4f8fb 0%,#ffffff 100%)}
  .brand{left:133px;top:30px;display:flex;align-items:center;gap:14px}
  .brand-mark{width:50px;height:50px;border-radius:50%;background:var(--green)}
  .brand-name{font-family:"Jost",Arial,sans-serif;font-weight:500;font-size:46px;color:var(--green-dark);letter-spacing:.5px}
  .search{left:845px;top:12px;width:240px;height:28px;border:1px solid var(--grey-light);background:#fff;font-size:12px;color:#9a9a9a;padding:5px 10px}
  .search svg{position:absolute;right:8px;top:6px}
  .nav{left:680px;top:68px;display:flex}
  .nav-item{height:62px;text-align:center;font-size:14px;color:var(--ink);padding-top:6px}
  .nav-item svg{display:block;margin:8px auto 0}
  .nav-item.is-active{width:110px;background:var(--green);color:#fff}
  .nav-item.about{width:120px}
  .nav-item.partners{width:80px}
  .nav-item.contact{width:90px}
  .header-rule{left:0;top:130px;width:1200px;height:4px;background:var(--green)}

  /* hero */
  .hero{left:0;top:134px;width:1200px;height:588px;background:radial-gradient(ellipse at 55% 35%,#fff3a0 0%,#f4da1c 35%,#d9b600 70%,#9c8a10 100%)}
  .hero-dots{left:126px;top:684px;display:flex;gap:8px}
  .hero-dots span{width:16px;height:16px;border-radius:50%;background:#bfe4f8;border:2px solid #5fb7e6}
  .hero-dots span:first-child{background:var(--blue)}
  .hero-rule{left:0;top:722px;width:1200px;height:4px;background:var(--green)}

  /* intro */
  .section-mark{width:34px;height:34px;border-radius:50%;background:var(--green);left:583px}
  .intro-title{left:0;width:1200px;text-align:center;font-family:"Jost",Arial,sans-serif;font-weight:400;font-size:38px;letter-spacing:1px;line-height:1}
  .intro-title.line-one{top:876px;color:var(--blue)}
  .intro-title.line-two{top:928px;color:var(--green-dark)}
  .intro-copy{left:240px;top:988px;width:720px;text-align:center;font-size:11px;line-height:17px;color:#9b9b9b}
  .btn{display:block;border:2px solid var(--green);background:#fff;color:#555;font-size:13px;text-align:center}
  .intro-btn{left:512px;top:1058px;width:146px;height:40px;line-height:36px}

  /* features */
  .features-rule{left:0;top:1155px;width:1200px;height:4px;background:var(--green)}
  .features{left:0;top:1159px;width:1200px;height:604px;background:radial-gradient(ellipse at 30% 30%,#f7d8c0 0%,#e2b79c 30%,#b6907c 60%,#7c6a5e 100%)}
  .features-title{left:0;top:1216px;width:1200px;text-align:center;font-family:"Jost",Arial,sans-serif;font-size:36px;line-height:42px;color:#111}
  .feature{width:200px;top:1346px}
  .feature-label{text-align:center;font-weight:700;font-size:19px;color:var(--blue-deep);height:34px}
  .feature-card{height:297px;border:4px solid var(--green-soft);background:rgba(255,255,255,.62);text-align:center}
  .feature-card svg{display:block;margin:28px auto 0}
  .feature-text{margin:26px 18px 0;font-size:11px;line-height:16px;color:#2b2b2b}
  .feature-btn{width:90px;height:30px;line-height:26px;margin:16px auto 0;border:1px solid #555;background:transparent;font-size:11px;color:#333}
  .features-bottom{left:0;top:1763px;width:1200px;height:3px;background:var(--green)}

  /* testimonials */
  .testimonial-title{left:0;top:1886px;width:1200px;text-align:center;font-family:"Jost",Arial,sans-serif;font-size:34px;color:var(--blue)}
  .testimonial{width:500px;height:150px}
  .avatar{position:absolute;left:0;top:0;width:144px;height:144px;border-radius:50%;border:4px solid #fff;box-shadow:0 0 0 2px #d5d5d5;background:linear-gradient(160deg,#c9d5df 0%,#9aaab6 55%,#5f6b78 100%)}
  .quote{position:absolute;left:152px;top:14px;width:330px;font-size:11px;line-height:16px;color:#555;padding-left:22px}
  .quote-open,.quote-close{position:absolute;font-family:Georgia,serif;font-size:44px;line-height:1;color:#cfcfcf}
  .quote-open{left:0;top:-8px}
  .quote-close{right:120px;bottom:-38px}

  /* footer */
  .site-footer{left:0;top:2405px;width:1200px;height:373px;background:var(--footer);overflow:hidden}
  .footer-brand{left:190px;top:105px;display:flex;align-items:center;gap:30px;opacity:.18}
  .footer-brand-mark{width:150px;height:150px;border-radius:50%;background:#fff}
  .footer-brand-name{font-family:"Jost",Arial,sans-serif;font-weight:500;font-size:150px;color:#fff;line-height:1}
  .social{left:533px;top:64px;display:flex;gap:14px}
  .social span{width:20px;height:20px;border-radius:50%;background:#fff}
  .footer-phone{left:0;top:136px;width:1200px;text-align:center;font-size:15px;color:#fff}
  .footer-phone svg{vertical-align:-3px;margin-right:6px}
  .footer-copy{left:0;top:192px;width:1200px;text-align:center;font-size:14px;font-weight:600;color:#fff}
  .footer-nav{left:0;top:250px;width:1200px;display:flex;justify-content:center;gap:26px;font-size:14px;font-weight:600;color:#fff}
</style>
</head>
<body>

<header class="abs site-header">
  <div class="abs brand"><span class="brand-mark"></span><span class="brand-name">LumaGrove</span></div>
  <div class="abs search">Search...
    <svg width="16" height="16" viewBox="0 0 16 16"><circle cx="6.5" cy="6.5" r="4.5" fill="none" stroke="#888" stroke-width="1.6"/><line x1="10" y1="10" x2="14.5" y2="14.5" stroke="#888" stroke-width="2"/></svg>
  </div>
  <nav class="abs nav">
    <div class="nav-item is-active">Home
      <svg width="26" height="22" viewBox="0 0 26 22"><path d="M13 1 1 11h4v10h6v-6h4v6h6V11h4z" fill="#fff"/></svg>
    </div>
    <div class="nav-item about">About us
      <svg width="26" height="18" viewBox="0 0 26 18"><rect x="1" y="1" width="24" height="16" fill="none" stroke="#222" stroke-width="2"/><rect x="4" y="4" width="7" height="8" fill="#222"/><rect x="13" y="5" width="9" height="2" fill="#222"/><rect x="13" y="10" width="9" height="2" fill="#222"/></svg>
    </div>
    <div class="nav-item partners">Partners
      <svg width="28" height="20" viewBox="0 0 28 20"><path d="M2 8 8 2l6 4 6-4 6 6-9 9-5-4-4 4z" fill="#222"/></svg>
    </div>
    <div class="nav-item contact">Contact
      <svg width="26" height="20" viewBox="0 0 26 20"><path d="M1 8 13 1l12 7v11H1z" fill="#222"/><path d="M3 9l10 6 10-6" fill="none" stroke="#fff" stroke-width="1.6"/></svg>
    </div>
  </nav>
</header>
<div class="abs header-rule"></div>

<section class="abs hero" role="img" aria-label="Photo of a young woman holding wildflowers in a bright yellow rapeseed field"></section>
<div class="abs hero-dots"><span></span><span></span><span></span><span></span></div>
<div class="abs hero-rule"></div>

<span class="abs section-mark" style="top:820px"></span>
<h1 class="abs intro-title line-one">YOU WILL LIKE TO LOOK LIKE</h1>
<h2 class="abs intro-title line-two">GODDES EVERY DAY!</h2>
<p class="abs intro-copy">Fresh meals, steady habits and honest guidance help you feel light, strong and bright. Join a circle of nutritionists and friends who share simple steps toward a fuller, healthier life every single day.</p>
<a class="abs btn intro-btn">Read More</a>

<div class="abs features-rule"></div>
<section class="abs features" role="img" aria-label="Soft blurred photo of a smiling person in warm peach light"></section>
<h2 class="abs features-title">Suspendisse potenti. Suspendisse<br>non fringilla nulla.</h2>

<div class="abs feature" style="left:133px">
  <div class="feature-label">NUTRITION</div>
  <div class="feature-card">
    <svg width="100" height="100" viewBox="0 0 100 100"><rect x="8" y="52" width="84" height="5" fill="#2aa3dc" transform="rotate(-12 50 55)"/><path d="M50 56 36 92h28z" fill="#2aa3dc"/><circle cx="76" cy="26" r="14" fill="#2aa3dc"/><rect x="22" y="12" width="5" height="38" fill="#2aa3dc"/><circle cx="24" cy="14" r="6" fill="#2aa3dc"/></svg>
    <p class="feature-text">Balanced plates built with seasonal produce and guidance from trusted nutritionists.</p>
    <a class="btn feature-btn">Read More</a>
  </div>
</div>
<div class="abs feature" style="left:381px">
  <div class="feature-label">ENERGY</div>
  <div class="feature-card">
    <svg width="100" height="100" viewBox="0 0 100 100"><path d="M82 14C62 16 46 30 38 48l14 14c18-8 32-24 30-48z" fill="#2aa3dc"/><path d="M38 48 24 50l-8 12 18-2zM52 62l-2 14-12 8 2-18z" fill="#2aa3dc"/><path d="M30 66 18 82l4-14z" fill="#2aa3dc"/><circle cx="62" cy="36" r="6" fill="#fff"/></svg>
    <p class="feature-text">Small daily rituals that keep your body charged from morning to night.</p>
    <a class="btn feature-btn">Read More</a>
  </div>
</div>
<div class="abs feature" style="left:628px">
  <div class="feature-label">EXERCISE</div>
  <div class="feature-card">
    <svg width="100" height="100" viewBox="0 0 100 100"><circle cx="66" cy="18" r="9" fill="#2aa3dc"/><path d="M44 34h26l-8 24 14 14-6 6-20-18 6-16H48l-8 10-6-4z" fill="#2aa3dc"/><path d="M52 62 42 86h-8l10-28z" fill="#2aa3dc"/><rect x="6" y="40" width="24" height="5" fill="#2aa3dc"/><rect x="2" y="52" width="26" height="5" fill="#2aa3dc"/><rect x="8" y="64" width="20" height="5" fill="#2aa3dc"/></svg>
    <p class="feature-text">Friendly routines for every level, from gentle walks to brisk runs.</p>
    <a class="btn feature-btn">Read More</a>
  </div>
</div>
<div class="abs feature" style="left:874px">
  <div class="feature-label">WELLNESS</div>
  <div class="feature-card">
    <svg width="100" height="100" viewBox="0 0 100 100"><circle cx="50" cy="18" r="10" fill="#2aa3dc"/><path d="M36 32h28l6 30H30z" fill="#2aa3dc"/><path d="M36 36 18 58l6 4 16-16zM64 36l18 22-6 4-16-16z" fill="#2aa3dc"/><ellipse cx="50" cy="74" rx="38" ry="12" fill="#2aa3dc"/></svg>
    <p class="feature-text">Rest, breathe and reset with mindful moments shared by our community.</p>
    <a class="btn feature-btn">Read More</a>
  </div>
</div>
<div class="abs features-bottom"></div>

<span class="abs section-mark" style="top:1838px"></span>
<h2 class="abs testimonial-title">Testimonial</h2>

<article class="abs testimonial" style="left:125px;top:1996px">
  <div class="avatar" role="img" aria-label="Portrait of a smiling member"></div>
  <p class="quote"><span class="quote-open">“</span>Since joining I plan my meals with a real nutritionist and finally understand what my body needs. The advice is clear, kind and easy to follow every week.<span class="quote-close">”</span></p>
</article>
<article class="abs testimonial" style="left:622px;top:1996px">
  <div class="avatar" role="img" aria-label="Portrait of a smiling member in a cap"></div>
  <p class="quote"><span class="quote-open">“</span>The community keeps me going. Sharing recipes and workouts with people who care has made healthy living feel fun instead of a chore for my whole family.<span class="quote-close">”</span></p>
</article>
<article class="abs testimonial" style="left:125px;top:2210px">
  <div class="avatar" role="img" aria-label="Portrait of a smiling member"></div>
  <p class="quote"><span class="quote-open">“</span>As a busy father I needed simple steps. The weekly plans fit my schedule and I have more energy for work, sport and the people I love.<span class="quote-close">”</span></p>
</article>
<article class="abs testimonial" style="left:622px;top:2210px">
  <div class="avatar" role="img" aria-label="Portrait of a smiling member in a cap"></div>
  <p class="quote"><span class="quote-open">“</span>I found a nutritionist close to home within minutes. Our chats are honest and encouraging, and my progress has been steady and lasting ever since.<span class="quote-close">”</span></p>
</article>

<footer class="abs site-footer">
  <div class="abs footer-brand"><span class="footer-brand-mark"></span><span class="footer-brand-name">LumaGrove</span></div>
  <div class="abs social" aria-label="Social links"><span></span><span></span><span></span><span></span></div>
  <p class="abs footer-phone"><svg width="20" height="16" viewBox="0 0 20 16"><path d="M2 4c5-4 11-4 16 0l-2 3-3-1V4H7v2L4 7z" fill="#fff"/><rect x="4" y="8" width="12" height="7" rx="1" fill="#fff"/></svg>1-800-555-0147</p>
  <p class="abs footer-copy">LumaGrove © 2014 All Rights Reserved</p>
  <nav class="abs footer-nav"><span>Home</span><span>About us</span><span>Partners</span><span>Contact</span></nav>
</footer>

</body>
</html>
```